New Web Design for Texas Lawyer

We need to update the look of https://www.delvorkhale.example/. Need to be same colors but new logo and style. Modern.
General Style and Professionalism
Maintain the general style that is liked.
Aim for a more formal and professional appearance.
Logo and Lawyer Information
Design a new logo.
Note that Lawyer Peter is no longer with the firm. The new lawyer should be prominently displayed on the right.
Homepage Features
Consider implementing a slider for video content.
Explore the idea of featuring 18 wheelers on the forefront of the homepage.
SEO Focus
Prioritize SEO efforts for Austin and the surrounding areas.
Design
Develop a new website design.
Ensure that testimonials are more prominently displayed on the homepage.
Core Values and Additional Content
Await core values information from Helen.
Add a ClipNest link to the website.
Incorporate new photography to enhance the site's visual appeal.
Testimonials and Results
Create more compelling testimonials.
Highlight case results to make them more appealing.
Media Page
Improve the media page for a better user experience.
Firm Recognition
Emphasize the firm's status as an award-winning law firm.
Referral Program
Make the "referral program" more prominent.
Emphasize the message about passive income and always include the relevant rule.
Attorney Pages
Design a main page for the attorney.
Create subpages for other lawyers.
About the Law Firm
Design a comprehensive "About the Law Firm" page.
Our 5 core values:
Integrity (we live up to our word, we say what we mean and mean what we say; we’re honest)
Compassion (we put people FIRST; we listen because we care)
Trust (earned through respect and communication)
Advocacy (we are the voice of those who can’t speak on their own behalf; we do it through experience, competency and hard work)
Results (we aim to achieve the most it takes to make our clients whole)
Number of Pages Required
4 page
Look and feel
Each slider illustrates characteristics of the customer's brand and the style your logo design should communicate.

```html
<!DOCTYPE html>
<html lang="en">
<head>
<meta charset="utf-8">
<title>Delvork Hale Law — Personal Injury Lawyers</title>
<link href="https://fonts.googleapis.com/css2?family=Open+Sans:wght@300;400;600;700&family=Tinos:wght@400;700&display=swap" rel="stylesheet">
<style>
:root{
  --navy:#1a3066;
  --navy-dark:#1b2a4a;
  --teal:#0aa5c6;
  --lavender:#f1eff7;
  --lavender-deep:#e9e3f3;
  --ink:#2b2f3a;
  --muted:#6d6f78;
  --footer:#262b35;
  --white:#ffffff;
  --star:#f07a18;
}
*{margin:0;padding:0;box-sizing:border-box}
html,body{width:1200px;height:4521px;overflow:hidden}
body{position:relative;font-family:"Open Sans",Arial,sans-serif;color:var(--ink);background:var(--white)}
.abs{position:absolute}
.serif{font-family:"Tinos","Times New Roman",serif}

/* header */
.site-header{position:absolute;left:0;top:0;width:1200px;height:125px;background:var(--white);z-index:5}
.contact-chip{position:absolute;top:20px;display:flex;align-items:center;gap:10px;font-size:10px;line-height:13px}
.contact-chip b{display:block;font-size:11px;color:#111}
.contact-chip span{color:var(--muted)}
.chip-icon{width:28px;height:28px;border-radius:50%;background:var(--navy);display:flex;align-items:center;justify-content:center}
.book-btn{position:absolute;left:880px;top:15px;width:184px;height:38px;border-radius:19px;background:var(--navy);color:#fff;font-size:11px;font-weight:700;display:flex;align-items:center;justify-content:center}
.main-nav a{position:absolute;top:89px;font-size:11px;color:#444;text-decoration:none}
.logo-tab{position:absolute;left:500px;top:0;width:200px;height:147px;background:#fff;border-radius:0 0 26px 26px;z-index:6;display:flex;flex-direction:column;align-items:center;justify-content:center;gap:6px}
.logo-tab .mark{width:44px;height:44px;border:2px solid var(--navy)}
.logo-tab .name{font-family:"Tinos",serif;font-size:11px;color:var(--navy);letter-spacing:.5px}

/* hero */
.hero{position:absolute;left:0;top:125px;width:1200px;height:760px;background:linear-gradient(100deg,#3a3e47 0%,#5f646d 45%,#8a8f98 75%,#6b7079 100%)}
.hero-eyebrow{position:absolute;left:84px;top:365px;color:#fff;font-size:19px;letter-spacing:6px;font-weight:600}
.hero-title{position:absolute;left:78px;top:410px;color:#fff;font-size:50px;font-weight:700;letter-spacing:.5px}
.hero-rule{position:absolute;left:84px;top:495px;width:698px;height:2px;background:rgba(255,255,255,.85)}
.hero-text{position:absolute;left:84px;top:526px;width:640px;color:#fff;font-size:15.5px;line-height:28px}
.btn{position:absolute;height:38px;border-radius:19px;font-size:13px;font-weight:700;display:flex;align-items:center;justify-content:center}
.btn-teal{background:var(--teal);color:#fff}
.btn-white{background:#fff;color:var(--navy)}

.seal{position:absolute;width:60px;height:60px;border-radius:50%;background:#fff;border:3px solid #e7e7ee;display:flex;align-items:center;justify-content:center;font-family:"Tinos",serif;font-size:11px;color:var(--navy);font-weight:700}

/* about */
.portrait-ring{position:absolute;left:82px;top:956px;width:474px;height:474px;border-radius:50%;border:7px solid #1f5fb0;border-left-color:transparent;transform:rotate(-20deg)}
.portrait{position:absolute;left:96px;top:970px;width:446px;height:446px;border-radius:50%;background:radial-gradient(circle at 50% 40%,#e9e9ea 0%,#d6d6d8 55%,#c59a2a 56%,#b98e20 100%)}
.eyebrow-teal{color:var(--teal);font-size:16px}
.h2{font-family:"Tinos","Times New Roman",serif;color:var(--navy);font-weight:400}
.body-text{font-size:13px;line-height:23.5px;color:#5d5f68;font-weight:300}
.quote-block{position:absolute;left:623px;top:1080px;width:470px;border-left:2px solid #333;padding-left:14px}

/* services */
.services{position:absolute;left:0;top:1509px;width:1200px;height:575px;background:var(--lavender)}
.center{text-align:center;left:0;width:1200px}
.sub{font-size:13px;line-height:23px;color:var(--muted);font-weight:300}
.service-card{position:absolute;top:1749px;width:320px;height:266px;overflow:hidden}
.service-card .label{position:absolute;left:20px;top:60px;color:#fff;font-family:"Tinos",serif;font-weight:700;font-size:29px}
.service-card .arrow{position:absolute;left:40px;top:215px}
.icon-disc{position:absolute;width:70px;height:70px;border-radius:50%;background:#fff;box-shadow:0 2px 8px rgba(0,0,0,.12);display:flex;align-items:center;justify-content:center;z-index:2}

/* why */
.why-blob-left{position:absolute;left:118px;top:2305px;width:470px;height:440px;border-radius:0 230px 230px 0;background:linear-gradient(90deg,rgba(240,236,248,0) 0%,#ece6f5 60%,#e3dbf0 100%)}
.why-blob-right{position:absolute;left:612px;top:2305px;width:470px;height:440px;border-radius:230px 0 0 230px;background:linear-gradient(270deg,rgba(240,236,248,0) 0%,#ece6f5 60%,#e3dbf0 100%)}
.why-photo{position:absolute;left:468px;top:2295px;width:264px;height:400px;border-radius:132px 132px 132px 132px;background:linear-gradient(180deg,#c8a57a 0%,#e8d9c8 25%,#3a3b44 55%,#23252d 100%)}
.feature{position:absolute;width:290px}
.feature h3{font-family:"Tinos",serif;font-weight:400;color:var(--navy);font-size:23px;margin-bottom:10px}
.feature p{font-size:12.5px;line-height:23px;color:var(--muted);font-weight:300}
.feature.left{text-align:right;left:88px}
.feature.right{left:798px}
.feat-icon{position:absolute;width:90px;height:90px;border-radius:50%;background:#fff;display:flex;align-items:center;justify-content:center}
.feat-icon span{width:76px;height:76px;border-radius:50%;background:#3d5486;border:3px solid #c6d2ea;display:flex;align-items:center;justify-content:center}

/* appointment */
.appointment{position:absolute;left:0;top:2813px;width:1200px;height:562px;background:linear-gradient(90deg,rgba(28,32,42,.92) 0%,rgba(40,44,56,.82) 45%,#6a6e78 100%)}
.hours-title{position:absolute;left:95px;top:2948px;color:#fff;font-family:"Tinos",serif;font-size:28px}
.hours{position:absolute;left:96px;top:3013px;width:457px;height:228px;border-left:4px solid var(--teal);background:linear-gradient(90deg,rgba(255,255,255,.07),rgba(255,255,255,0))}
.hours-row{position:absolute;left:36px;right:0;display:flex;justify-content:space-between;color:#fff;font-size:14px}
.hours-row b{font-weight:600}
.hours-row span{color:#d8d8de}
.form-panel{position:absolute;left:612px;top:2841px;width:490px;height:495px;background:var(--lavender-deep)}
.field{position:absolute;height:52px;background:#fff;font-size:13px;color:#333;padding-left:26px;display:flex;align-items:center}
.submit{position:absolute;left:54px;top:423px;width:385px;height:55px;background:var(--teal);color:#fff;font-size:19px;font-weight:700;display:flex;align-items:center;justify-content:center}

/* reviews */
.reviews{position:absolute;left:0;top:3375px;width:1200px;height:700px;background:#f4f1f8}
.review-card{position:absolute;top:3654px;width:320px;height:266px;background:#fff;padding:50px 26px 0}
.review-card.active{border-bottom:4px solid var(--navy-dark)}
.avatar{position:absolute;left:34px;top:-32px;width:62px;height:62px;border-radius:50%;background:linear-gradient(160deg,#d9c4b2,#8a7b70);border:4px solid #fff;box-shadow:0 1px 4px rgba(0,0,0,.15)}
.quote-mark{position:absolute;right:34px;top:-22px;font-family:"Tinos",serif;font-size:100px;line-height:80px;color:#7ad0e6;font-weight:700}
.stars{color:var(--star);font-size:15px;letter-spacing:3px}
.review-card p{margin-top:10px;font-size:12.5px;line-height:23px;color:var(--muted);font-weight:300}
.review-card h4{margin-top:12px;font-family:"Tinos",serif;font-weight:400;font-size:21px;color:#222}
.review-card small{display:block;margin-top:4px;font-size:9.5px;color:#5a3ea0;letter-spacing:.5px}

/* footer */
.footer{position:absolute;left:0;top:3990px;width:1200px;height:531px;background:var(--footer)}
.footer-logo{position:absolute;left:545px;top:4150px;width:110px;text-align:center;color:#fff}
.footer-logo .mark{width:44px;height:44px;border:2px solid #fff;margin:0 auto 6px}
.footer-logo .name{font-family:"Tinos",serif;font-size:10px}
.footer-nav a{position:absolute;top:4280px;color:#fff;font-size:14px;text-decoration:none}
.footer-rule{position:absolute;left:140px;top:4333px;width:920px;height:1px;background:#4a4f5b}
.f-contact{position:absolute;top:4380px;display:flex;align-items:center;gap:14px;color:#fff;font-size:12px;line-height:17px}
.f-contact .ring{width:54px;height:54px;border-radius:50%;border:2px solid #8e929c;display:flex;align-items:center;justify-content:center}
.f-divider{position:absolute;top:4373px;width:1px;height:64px;background:#5a5f6a}
.bottom-bar{position:absolute;left:0;top:4464px;width:1200px;height:57px;background:var(--navy-dark)}
.bottom-bar .brand{position:absolute;left:147px;top:20px;color:#fff;font-size:12px;font-weight:600}
.social{position:absolute;top:16px;width:25px;height:25px;border:1px solid #cfd4e0}
</style>
</head>
<body>

<header class="site-header">
  <div class="contact-chip" style="left:124px">
    <div class="chip-icon"><svg width="14" height="14" viewBox="0 0 24 24"><path fill="#fff" d="M6.6 10.8a15 15 0 006.6 6.6l2.2-2.2c.3-.3.7-.4 1-.2 1.1.4 2.3.6 3.6.6.6 0 1 .4 1 1V20c0 .6-.4 1-1 1A17 17 0 013 4c0-.6.4-1 1-1h3.5c.6 0 1 .4 1 1 0 1.3.2 2.5.6 3.6.1.3 0 .7-.2 1z"/></svg></div>
    <div><b>Call Us:</b><span>(555) 014 2290</span></div>
  </div>
  <div class="contact-chip" style="left:282px">
    <div class="chip-icon"><svg width="14" height="14" viewBox="0 0 24 24"><path fill="#fff" d="M3 5h18v14H3z M3 5l9 7 9-7" stroke="#1a3066" stroke-width="1.5"/></svg></div>
    <div><b>Email:</b><span>office@delvorkhale.example</span></div>
  </div>
  <nav class="main-nav">
    <a href="#" style="left:126px">Home</a>
    <a href="#" style="left:238px">About Us</a>
    <a href="#" style="left:388px">Services</a>
    <a href="#" style="left:706px">Cases</a>
    <a href="#" style="left:834px">Blog</a>
    <a href="#" style="left:959px">Contact Us</a>
  </nav>
  <div class="book-btn">BOOK APPOINTMENT</div>
</header>
<div class="logo-tab">
  <div class="mark"></div>
  <div class="name">DELVORK HALE LAW, PLLC</div>
</div>

<section class="hero" role="img" aria-label="Photo of lawyers meeting around an office table"></section>
<div class="hero-eyebrow">PERSONAL INJURY LAWYERS</div>
<h1 class="hero-title">Your Advocate in Tough Times</h1>
<div class="hero-rule"></div>
<p class="hero-text">Lorem ipsum dolor sit amet, consectetur adipiscing elit, sed do eiusmod tempor incididunt ut labore et dolore magna</p>
<div class="btn btn-teal" style="left:84px;top:614px;width:144px">LEARN MORE</div>
<div class="btn btn-white" style="left:240px;top:614px;width:179px">REQUEST QUOTE</div>

<svg class="abs" style="left:0;top:780px" width="1200" height="140" viewBox="0 0 1200 140">
  <path d="M0 10 Q600 190 1200 10 L1200 140 L0 140 Z" fill="#fff"/>
  <path d="M270 78 Q600 120 955 78" fill="none" stroke="var(--teal)" stroke-width="3"/>
</svg>
<div class="seal" style="left:570px;top:865px">DH</div>

<!-- about -->
<div class="portrait-ring"></div>
<div class="portrait" role="img" aria-label="Portrait of a smiling lawyer in a yellow blazer"></div>
<div class="abs eyebrow-teal serif" style="left:623px;top:976px">Injury Victims Deserve Justice</div>
<h2 class="abs h2" style="left:623px;top:1015px;font-size:34px">Your Voice in the Courtroom</h2>
<div class="quote-block body-text">Lorem ipsum dolor sit amet, consectetur adipiscing elit, sed do eiusmod or incididunt ut labore et dolore</div>
<p class="abs body-text" style="left:623px;top:1161px;width:470px">Lorem ipsum dolor sit amet, consectetur adipiscing elit, sed do eiusmod obgr incididunt ut labore et dolore Lorem ipsum dolor sit amet, consectetur adip iscing elit, sed do eiusmod tempor incididunt ut labore et dolore m agna aliqua. Ut enim ad minim veniam, quis nostrud exercitation ullamco laboris nisi ut aliquip ex ea commodo consequat.</p>
<p class="abs body-text" style="left:623px;top:1294px;width:470px">Lorem ipsum dolor sit amet, consectetur adipiscing elit, sed do eiusmod obgr incididunt ut labore et dolore Lorem ipsum dol</p>
<div class="abs" style="left:619px;top:1359px;width:141px;height:44px;background:var(--teal);color:#fff;font-weight:700;font-size:15px;display:flex;align-items:center;justify-content:center;border-radius:0 14px 0 14px">Contact us</div>

<!-- services -->
<section class="services"></section>
<h2 class="abs h2 center" style="top:1562px;font-size:45px">Our Services</h2>
<p class="abs sub center" style="top:1627px">Lorem ipsum dolor sit amet, consectetur adipiscing elit, sed do eiusmod temp<br>or incididunt ut labore et dolore</p>

<div class="service-card" style="left:93px;background:linear-gradient(135deg,#5d6068,#2f3138)" role="img" aria-label="Damaged car after an accident"><div class="label">Car Accidents</div><svg class="arrow" width="44" height="14"><path d="M0 7H42M34 1l8 6-8 6" stroke="#fff" stroke-width="2" fill="none"/></svg></div>
<div class="service-card" style="left:440px;background:linear-gradient(135deg,#6d6e70,#3b3c3e)" role="img" aria-label="Injured worker on a construction site"><div class="label">Workplace Accidents</div><svg class="arrow" width="44" height="14"><path d="M0 7H42M34 1l8 6-8 6" stroke="#fff" stroke-width="2" fill="none"/></svg></div>
<div class="service-card" style="left:788px;background:linear-gradient(135deg,#3c5270,#22344f)" role="img" aria-label="Work safety concept graphic"><div class="label">Wrongful Death</div><svg class="arrow" width="44" height="14"><path d="M0 7H42M34 1l8 6-8 6" stroke="#fff" stroke-width="2" fill="none"/></svg></div>

<div class="icon-disc" style="left:137px;top:1714px"><svg width="32" height="32" viewBox="0 0 32 32" fill="none" stroke="var(--navy)" stroke-width="2"><circle cx="14" cy="14" r="11"/><circle cx="22" cy="22" r="5"/></svg></div>
<div class="icon-disc" style="left:485px;top:1714px"><svg width="32" height="32" viewBox="0 0 32 32" fill="none" stroke="var(--navy)" stroke-width="2"><circle cx="16" cy="16" r="10"/><circle cx="16" cy="16" r="4"/><path d="M16 2v6M16 24v6M2 16h6M24 16h6"/></svg></div>
<div class="icon-disc" style="left:833px;top:1714px"><svg width="32" height="32" viewBox="0 0 32 32" fill="none" stroke="var(--navy)" stroke-width="2"><path d="M6 26h20M10 20l8-12 4 4-8 10z"/></svg></div>

<!-- why -->
<h2 class="abs h2 center" style="top:2138px;font-size:45px">Why Choose Us</h2>
<p class="abs sub center" style="top:2204px">Lorem ipsum dolor sit amet, consectetur adipiscing elit, sed do eiusmod temp<br>or incididunt ut labore et dolore</p>
<div class="why-blob-left"></div>
<div class="why-blob-right"></div>
<div class="why-photo" role="img" aria-label="Portrait of a confident lawyer with arms crossed"></div>

<div class="feature left" style="top:2360px"><h3>In-Depth Knowledge</h3><p>Lorem ipsum dolor sit amet, conser adi<br>or incididunt ut labore et dolore</p></div>
<div class="feature left" style="top:2491px"><h3>Client-Centric</h3><p>Lorem ipsum dolor sit amet, conser adi<br>or incididunt ut labore et dolore</p></div>
<div class="feature left" style="top:2624px"><h3>Personalized Approach</h3><p>Lorem ipsum dolor sit amet, conser adi<br>or incididunt ut labore et dolore</p></div>
<div class="feature right" style="top:2360px"><h3>Proven Track Record</h3><p>Lorem ipsum dolor sit amet, conser adi<br>or incididunt ut labore et dolore</p></div>
<div class="feature right" style="top:2491px"><h3>Maximized Compensation</h3><p>Lorem ipsum dolor sit amet, conser adi<br>or incididunt ut labore et dolore</p></div>
<div class="feature right" style="top:2624px"><h3>In-Depth Knowledge</h3><p>Lorem ipsum dolor sit amet, conser adi<br>or incididunt ut labore et dolore</p></div>

<div class="feat-icon" style="left:397px;top:2358px"><span><svg width="30" height="30" viewBox="0 0 30 30" fill="none" stroke="#fff" stroke-width="2"><path d="M5 22a11 11 0 1120 0"/><path d="M15 18l5-6"/></svg></span></div>
<div class="feat-icon" style="left:397px;top:2490px"><span><svg width="30" height="30" viewBox="0 0 30 30" fill="none" stroke="#fff" stroke-width="2"><circle cx="15" cy="15" r="5"/><circle cx="15" cy="15" r="11" stroke-dasharray="4 3"/></svg></span></div>
<div class="feat-icon" style="left:397px;top:2623px"><span><svg width="30" height="30" viewBox="0 0 30 30" fill="none" stroke="#fff" stroke-width="2"><path d="M4 26h22M9 20l8-12 4 4-8 10z"/></svg></span></div>
<div class="feat-icon" style="left:688px;top:2358px"><span><svg width="30" height="30" viewBox="0 0 30 30" fill="none" stroke="#fff" stroke-width="2"><path d="M15 3l3.5 7.5 8 1-6 5.5 1.6 8L15 21l-7 4 1.5-8-6-5.5 8-1z"/></svg></span></div>
<div class="feat-icon" style="left:688px;top:2490px"><span><svg width="30" height="30" viewBox="0 0 30 30" fill="none" stroke="#fff" stroke-width="2"><path d="M25 13a10 10 0 00-18-4M5 17a10 10 0 0018 4M7 3v6h6M23 27v-6h-6"/></svg></span></div>
<div class="feat-icon" style="left:688px;top:2623px"><span><svg width="30" height="30" viewBox="0 0 30 30" fill="none" stroke="#fff" stroke-width="2"><circle cx="11" cy="10" r="4"/><circle cx="21" cy="12" r="3"/><path d="M3 25c0-5 4-8 8-8s8 3 8 8M19 19c4 0 8 2 8 6"/></svg></span></div>

<!-- appointment -->
<section class="appointment" role="img" aria-label="Photo of smiling clients and lawyers in a meeting"></section>
<h2 class="hours-title">Opening Hours</h2>
<div class="hours">
  <div class="hours-row" style="top:32px"><b>Monday - Thursday</b><span>08am - 05pm</span></div>
  <div class="hours-row" style="top:82px"><b>Saturday</b><span>08am - 02pm</span></div>
  <div class="hours-row" style="top:132px"><b>Phone</b><span>+123 456 7890</span></div>
  <div class="hours-row" style="top:183px"><b>Email</b><span>info@company.com</span></div>
</div>
<form class="form-panel">
  <div class="abs" style="left:54px;top:40px;width:52px;height:52px;border-radius:50%;background:var(--navy-dark);display:flex;align-items:center;justify-content:center"><svg width="24" height="24" viewBox="0 0 24 24" fill="none" stroke="#fff" stroke-width="1.6"><rect x="3" y="5" width="18" height="15"/><path d="M3 10h18M8 3v4M16 3v4"/></svg></div>
  <div class="abs" style="left:121px;top:36px;font-size:13px;color:#555">Get in touch with us any day any time</div>
  <div class="abs serif" style="left:121px;top:58px;font-size:32px;color:var(--navy-dark)">Make Appointment</div>
  <div class="field" style="left:54px;top:134px;width:183px">First Name</div>
  <div class="field" style="left:254px;top:134px;width:185px">Last Name</div>
  <div class="field" style="left:54px;top:206px;width:183px">Email Address</div>
  <div class="field" style="left:254px;top:206px;width:185px">Phone Number</div>
  <div class="field" style="left:54px;top:278px;width:385px">Select Subject</div>
  <div class="field" style="left:54px;top:351px;width:385px">dd/mm/yyyy</div>
  <div class="submit">SUBMIT</div>
</form>

<!-- reviews -->
<section class="reviews"></section>
<h2 class="abs h2 center" style="top:3457px;font-size:45px;color:#1d2230">Clients Review</h2>
<p class="abs sub center" style="top:3523px">Lorem ipsum dolor sit amet, consectetur adipiscing elit, sed do eiusmod temp<br>or incididunt ut labore et dolore</p>

<article class="review-card" style="left:102px">
  <div class="avatar" role="img" aria-label="Client photo"></div><div class="quote-mark">&rdquo;</div>
  <div class="stars">★★★★★</div>
  <p>Lorem ipsum dolor sit amet, consectetur adipiscing elit, sed do eiusmod or incididun t ut labore et dolore Lorem ipsum dolor sit adipiscing elit, sed do ehjhj</p>
  <h4>Mara Quillen</h4><small>BUSINESSMAN</small>
</article>
<article class="review-card active" style="left:445px">
  <div class="avatar" role="img" aria-label="Client photo"></div><div class="quote-mark" style="color:var(--navy)">&rdquo;</div>
  <div class="stars">★★★★★</div>
  <p>Lorem ipsum dolor sit amet, consectetur adipiscing elit, sed do eiusmod or incididun t ut labore et dolore Lorem ipsum dolor sit adipiscing elit, sed do ehjhj</p>
  <h4>Mara Quillen</h4><small>BUSINESSMAN</small>
</article>
<article class="review-card" style="left:788px">
  <div class="avatar" role="img" aria-label="Client photo"></div><div class="quote-mark">&rdquo;</div>
  <div class="stars">★★★★★</div>
  <p>Lorem ipsum dolor sit amet, consectetur adipiscing elit, sed do eiusmod or incididun t ut labore et dolore Lorem ipsum dolor sit adipiscing elit, sed do ehjhj</p>
  <h4>Mara Quillen</h4><small>BUSINESSMAN</small>
</article>

<!-- footer -->
<footer class="footer"></footer>
<svg class="abs" style="left:0;top:3985px" width="1200" height="110" viewBox="0 0 1200 110">
  <path d="M0 0 H1200 V5 Q600 120 0 5 Z" fill="#f4f1f8"/>
  <path d="M245 40 Q600 88 955 40" fill="none" stroke="var(--teal)" stroke-width="3"/>
</svg>
<div class="seal" style="left:575px;top:4036px">DH</div>
<div class="footer-logo"><div class="mark"></div><div class="name">DELVORK HALE LAW, PLLC</div></div>
<nav class="footer-nav">
  <a href="#" style="left:334px">HOME</a>
  <a href="#" style="left:427px">SERVICES</a>
  <a href="#" style="left:533px">ABOUT US</a>
  <a href="#" style="left:652px">TESTIMONIALS</a>
  <a href="#" style="left:803px">BLOG</a>
</nav>
<div class="footer-rule"></div>
<div class="f-contact" style="left:180px"><div class="ring"><svg width="26" height="26" viewBox="0 0 26 26" fill="none" stroke="#fff" stroke-width="1.5"><circle cx="13" cy="13" r="10"/><path d="M3 13h20M13 3c4 4 4 16 0 20M13 3c-4 4-4 16 0 20"/></svg></div><div>123, Building Name, Street<br>City, State XY 123456</div></div>
<div class="f-divider" style="left:430px"></div>
<div class="f-contact" style="left:510px"><div class="ring"><svg width="22" height="26" viewBox="0 0 22 26" fill="none" stroke="#fff" stroke-width="1.5"><rect x="5" y="2" width="12" height="22" rx="2"/><path d="M9 20h4"/></svg></div><div>PHONE<br>(123) 456 7890</div></div>
<div class="f-divider" style="left:749px"></div>
<div class="f-contact" style="left:833px"><div class="ring"><svg width="26" height="22" viewBox="0 0 26 22" fill="none" stroke="#fff" stroke-width="1.5"><rect x="2" y="3" width="22" height="16"/><path d="M2 3l11 9 11-9"/></svg></div><div>EMAIL<br>info@company.com</div></div>

<div class="bottom-bar">
  <div class="brand">Delvork Hale Law</div>
  <a class="social" href="#" style="left:935px" aria-label="Social profile"></a>
  <a class="social" href="#" style="left:967px" aria-label="Social profile"></a>
  <a class="social" href="#" style="left:999px" aria-label="Social profile"></a>
  <a class="social" href="#" style="left:1031px" aria-label="Social profile"></a>
</div>

</body>
</html>
```